Website design for an Italian restaurant in Amsterdam

I need a design for a client of mine. It is for Teatro Lunaverde, an Italian restaurant in Amsterdam.
We are going for a clean, modern look but we also need to realise an authentic feel.
The restaurant is located in an old movie theatre, that is where the name Teatro Lunaverde comes from.
Industry/Entity Type
Italian Restaurant
Number of Pages Required
1 page
Font styles to use
Sans Serif
Colors
Designer to choose colors to be used in the design.

```html
<!DOCTYPE html>
<html lang="en">
<head>
<meta charset="utf-8">
<title>Teatro Lunaverde – Italian Restaurant Amsterdam</title>
<link rel="stylesheet" href="https://fonts.googleapis.com/css2?family=Playfair+Display:wght@400;700&family=Questrial&display=swap">
<style>
:root{
  --wine:#a94d58;
  --wine-dark:#8e3c47;
  --ink:#151515;
  --night:#0d0d0d;
  --paper:#efeeec;
  --white:#ffffff;
  --muted:#6a6a6a;
  --line:#d9d9d9;
  --serif:"Playfair Display", Georgia, serif;
  --sans:"Questrial", "Century Gothic", Arial, sans-serif;
}
*{box-sizing:border-box;margin:0;padding:0}
html,body{width:1200px;height:3030px;overflow:hidden}
body{font-family:var(--sans);color:var(--ink);background:var(--paper);position:relative}
.abs{position:absolute}
.section-title{font-family:var(--serif);font-weight:700;font-size:27px;text-transform:uppercase;text-align:center;letter-spacing:.5px}
.section-title::after{content:"";display:block;width:30px;height:2px;background:currentColor;margin:12px auto 0}
.btn{display:inline-block;border-radius:20px;font-size:12px;letter-spacing:1px;text-transform:uppercase;padding:0 26px;height:32px;line-height:32px;font-weight:700}
.btn-solid{background:var(--wine);color:var(--white)}
.btn-ghost{border:2px solid var(--wine);color:var(--wine);line-height:28px}

/* header */
.site-header{top:0;left:0;width:1200px;height:100px;background:var(--night)}
.brand{left:205px;top:20px;width:150px;text-align:center;color:var(--white)}
.brand-dot{width:26px;height:26px;border-radius:50%;background:var(--wine);margin:0 auto 6px}
.brand-name{font-family:var(--serif);font-size:15px;letter-spacing:.5px;color:var(--white);text-transform:uppercase}
.brand-tag{font-size:8px;color:#999;margin-top:2px}
.topbar{top:16px;left:670px;display:flex;gap:8px;align-items:center}
.pill{height:24px;border:1px solid #777;border-radius:12px;color:var(--white);font-size:12px;display:flex;align-items:center;gap:6px;padding:0 10px}
.round{width:24px;height:24px;border:1px solid #777;border-radius:50%;display:flex;align-items:center;justify-content:center}
.round span{width:7px;height:7px;background:#ccc;border-radius:50%}
.main-nav{top:62px;left:443px;display:flex;gap:30px;font-family:var(--serif);font-size:11.5px;text-transform:uppercase;color:var(--white);letter-spacing:.5px}
.main-nav a{position:relative}
.main-nav a.active{color:var(--wine)}

/* hero */
.hero{top:100px;left:0;width:1200px;height:460px;background:linear-gradient(100deg,#6b5040 0%,#a07a5a 30%,#7b3a2c 60%,#3d2a22 100%)}
.hero-line1{left:205px;top:310px;font-family:var(--serif);font-size:42px;color:var(--white);text-transform:uppercase}
.hero-line2{left:210px;top:372px;background:rgba(140,50,60,.85);font-family:var(--serif);font-size:38px;color:var(--white);text-transform:uppercase;padding:4px 16px}

/* welcome */
.welcome{top:560px;left:0;width:1200px;height:330px;text-align:center}
.welcome h2{font-family:var(--serif);font-size:18px;font-weight:700;text-transform:uppercase;margin-top:50px}
.welcome h3{font-family:var(--serif);font-size:19px;font-weight:400;color:var(--wine);text-transform:uppercase;margin-top:4px}
.welcome h3::after{content:"";display:block;width:30px;height:2px;background:var(--wine);margin:10px auto 0}
.welcome .lead{font-size:10.5px;font-weight:700;margin:14px auto 0;width:780px}
.welcome .body{font-size:10.5px;line-height:1.75;margin:6px auto 0;width:780px;color:#333}
.welcome .actions{margin-top:18px;display:flex;gap:10px;justify-content:center}

/* menu */
.menu{top:890px;left:0;width:1200px;height:570px;background:linear-gradient(180deg,#1a1612,#2a211b 50%,#14110f);color:var(--white)}
.menu .section-title{margin-top:50px}
.menu-tabs{top:110px;left:0;width:1200px;display:flex;justify-content:center;gap:30px;font-size:14px}
.menu-tabs .active{color:var(--wine);border-bottom:2px solid var(--wine);padding-bottom:4px}
.card{top:160px;width:240px;height:305px;background:var(--white);color:var(--ink);text-align:center}
.card h4{font-family:var(--serif);font-size:15px;font-weight:400;margin-top:30px}
.card p{font-size:11px;line-height:1.4;color:#555;margin:6px auto 0;width:160px}
.card .price{font-size:13px;font-weight:700;margin-top:4px}
.card .photo{position:absolute;left:0;width:240px;height:165px}
.card-1 .photo,.card-3 .photo{bottom:0}
.card-2 .photo{top:0}
.card-2 .info{position:absolute;top:165px;left:0;width:240px}
.card-2 .info h4{margin-top:22px}
.card-2 .info::before{content:"";position:absolute;top:-8px;left:112px;border-left:8px solid transparent;border-right:8px solid transparent;border-bottom:8px solid var(--white)}
.slide-arrow{top:290px}
.menu .btn{position:absolute;top:490px;left:541px}

/* group menu */
.group{top:1460px;left:0;width:1200px;height:470px}
.group .section-title{color:var(--wine);margin-top:52px}
.group-card{top:118px;left:262px;width:676px;height:292px;background:var(--white);box-shadow:0 2px 8px rgba(0,0,0,.15)}
.group-card .photo{position:absolute;left:0;top:0;width:343px;height:292px;background:linear-gradient(120deg,#d9d5c9,#b59474 45%,#7e5f47)}
.group-card .list{position:absolute;left:368px;top:18px;width:290px}
.group-card h4{font-family:var(--serif);font-size:16px;font-weight:400}
.group-card h5{font-size:15px;font-weight:400;margin:4px 0 8px}
.dish{margin-bottom:8px;font-size:11px;line-height:1.3}
.dish b{display:block}
.circle-arrow{width:22px;height:22px;border:1px solid #888;border-radius:50%;display:flex;align-items:center;justify-content:center}

/* reservation */
.reservation{top:1930px;left:0;width:1200px;height:315px;background:linear-gradient(180deg,#9d4853,#b25862 50%,#9a4550);color:var(--white)}
.reservation .section-title{margin-top:50px}
.res-form{top:2048px;left:210px;width:780px;height:222px;background:var(--white);box-shadow:0 2px 10px rgba(0,0,0,.2);padding:18px 54px;color:#555;font-size:11.5px}
.field{position:absolute;border-bottom:1px solid var(--line);height:24px;display:flex;justify-content:space-between;align-items:flex-start}
.field i{width:8px;height:8px;background:#999;border-radius:2px;margin-top:3px}
.res-form .btn-block{position:absolute;left:54px;top:146px;width:672px;height:32px;background:var(--wine);color:var(--white);font-size:12px;text-transform:uppercase;text-align:center;line-height:32px;font-weight:700;letter-spacing:1px}

/* gallery */
.gallery{top:2270px;left:0;width:1200px;height:470px}
.gallery .section-title{color:var(--wine);margin-top:44px}
.grid{top:2375px;left:210px;width:780px;height:310px;display:grid;grid-template-columns:repeat(4,1fr);grid-template-rows:repeat(2,1fr)}
.tile{position:relative}
.tile.hover{background:rgba(120,50,55,.92);color:var(--white);font-size:10.5px;text-align:center;display:flex;flex-direction:column;align-items:center;justify-content:center;gap:8px;padding:0 30px}
.plus{width:20px;height:20px;border:1px solid var(--white);border-radius:50%;display:flex;align-items:center;justify-content:center;font-size:14px}

/* footer */
.site-footer{top:2740px;left:0;width:1200px;height:250px;background:linear-gradient(180deg,#111,#1b1713);color:#ddd;font-size:11.5px}
.col{top:45px}
.col h6{font-family:var(--serif);font-size:13px;font-weight:400;text-transform:uppercase;color:var(--white);margin-bottom:14px;letter-spacing:.5px}
.links li{list-style:none;margin-bottom:8px}
.links li::before{content:"›";margin-right:8px}
.contact-row{display:flex;gap:10px;margin-bottom:12px;line-height:1.4}
.contact-row svg{flex:none}
.hours td{padding:0 0 5px 0}
.hours td:first-child{width:90px}
.news input{display:block;width:152px;height:26px;background:transparent;border:1px solid #555;color:#ccc;font-family:var(--sans);font-size:10px;padding:0 6px;margin-bottom:8px}
.news .sub{width:152px;height:24px;background:var(--wine);color:var(--white);text-align:center;line-height:24px;font-size:10.5px;text-transform:uppercase;font-weight:700}
.copyright{top:2990px;left:0;width:1200px;height:40px;background:var(--wine-dark);color:#eee;font-size:9.5px;text-align:center;line-height:40px}
</style>
</head>
<body>

<header class="site-header abs">
  <div class="brand abs">
    <div class="brand-dot"></div>
    <div class="brand-name">Teatro Lunaverde</div>
    <div class="brand-tag">Ristorante Italiano</div>
  </div>
  <div class="topbar abs">
    <div class="pill">
      <svg width="10" height="10" viewBox="0 0 10 10"><path d="M2 1l2 2-1 1.2a6 6 0 0 0 2.8 2.8L7 6l2 2-1.4 1.4C4.6 9.2.8 5.4.6 2.4z" fill="#fff"/></svg>
      (+31) 20 555 0192
    </div>
    <div class="round"><span></span></div>
    <div class="round"><span></span></div>
    <div class="round"><span></span></div>
    <div class="pill" style="font-size:10px"><span style="width:8px;height:8px;border-radius:50%;background:var(--wine)"></span>ENG</div>
  </div>
  <nav class="main-nav abs">
    <a class="active">Home</a><a>About Us</a><a>Menu</a><a>Groupmenu</a><a>Reservation</a><a>Contact Us</a>
  </nav>
</header>

<section class="hero abs" role="img" aria-label="Restaurant dining room with white tablecloths, red chairs and brick walls">
  <div class="hero-line1 abs">Lindengracht 74</div>
  <div class="hero-line2 abs">In the City Center</div>
</section>

<section class="welcome abs">
  <h2>Welcome to</h2>
  <h3>Teatro Lunaverde Italian Restaurant</h3>
  <p class="lead">Honest Italian cooking served in the grand hall of a former movie theatre, right in the heart of Amsterdam.</p>
  <p class="body">Our kitchen follows old family recipes from the south of Italy, made with fresh pasta, seasonal produce and carefully chosen wines. Take a seat beneath the original theatre ceiling and enjoy a slow dinner with friends, a quick lunch between meetings or a festive evening for your whole group. Every plate is prepared to order, and our staff will gladly guide you through the menu and the wine list.</p>
  <div class="actions"><span class="btn btn-solid">Read More</span><span class="btn btn-ghost">Book Now</span></div>
</section>

<section class="menu abs">
  <h2 class="section-title">Our Menu</h2>
  <div class="menu-tabs abs">
    <span>‹&nbsp; Antipasti</span><span>Le Insalate</span><span class="active">Le Paste</span><span>Il Pesce</span><span>La Carne &nbsp;›</span>
  </div>
  <svg class="slide-arrow abs" style="left:160px" width="14" height="60" viewBox="0 0 14 60"><path d="M12 2L2 30l10 28" stroke="#ccc" stroke-width="2" fill="none"/></svg>
  <svg class="slide-arrow abs" style="left:1026px" width="14" height="60" viewBox="0 0 14 60"><path d="M2 2l10 28L2 58" stroke="#ccc" stroke-width="2" fill="none"/></svg>
  <article class="card card-1 abs" style="left:222px">
    <h4>Lasagna al Forno</h4><p>Homemade lasagna from the oven</p><div class="price">€ 14,50</div>
    <div class="photo" role="img" aria-label="Lasagna with basil" style="background:linear-gradient(135deg,#6b8a3a,#c4552c 50%,#8a3a20)"></div>
  </article>
  <article class="card card-2 abs" style="left:480px">
    <div class="photo" role="img" aria-label="Ravioli with mushrooms" style="background:linear-gradient(135deg,#e0c56a,#b58a3a 50%,#5b4a33)"></div>
    <div class="info"><h4>Ravioli ai Funghi</h4><p style="width:180px">Green ravioli stuffed with spinach and ricotta cheese, in a creamy mushroom and parmigiano sauce</p><div class="price">€ 14,25</div></div>
  </article>
  <article class="card card-3 abs" style="left:738px">
    <h4>Bucatini Amatriciana</h4><p>Bucatini met tomatensaus, spek en ui</p><div class="price">€ 14,50</div>
    <div class="photo" role="img" aria-label="Grilled meat with vegetables" style="background:linear-gradient(135deg,#d9d6cc,#6b4a38 50%,#8fa05a)"></div>
  </article>
  <span class="btn btn-solid">View All</span>
</section>

<section class="group abs">
  <h2 class="section-title">Group Menu</h2>
  <div class="circle-arrow abs" style="left:215px;top:252px"><svg width="8" height="8" viewBox="0 0 8 8"><path d="M6 1L2 4l4 3" stroke="#666" fill="none"/></svg></div>
  <div class="circle-arrow abs" style="left:960px;top:252px"><svg width="8" height="8" viewBox="0 0 8 8"><path d="M2 1l4 3-4 3" stroke="#666" fill="none"/></svg></div>
  <div class="group-card abs" style="top:118px">
    <div class="photo" role="img" aria-label="Group of friends dining together"></div>
    <div class="list">
      <h4>Groupmenu Speciale (€ 34,50)</h4>
      <h5>Antipasti</h5>
      <div class="dish"><b>Bruschette al Pomodoro</b>Original Italian starter</div>
      <div class="dish"><b>Carpaccio con Crema di Tartufo</b>Thinly sliced fillet of beef in truffle cream</div>
      <div class="dish"><b>Vitello Tonnato</b>Thinly sliced veal in tuna sauce</div>
      <div class="dish"><b>Mozzarella Caprese</b>Fresh mozzarella with tomato and basil</div>
      <div class="dish"><b>Melanzane alla Parmigiana</b>Aubergine met mozzarella, parmezaanse kaas en tomatensaus uit de oven</div>
    </div>
  </div>
</section>

<section class="reservation abs">
  <h2 class="section-title">Reservation</h2>
</section>
<form class="res-form abs">
  <div class="field" style="left:54px;top:12px;width:320px"><span>Name</span><i></i></div>
  <div class="field" style="left:406px;top:12px;width:320px"><span>Email</span><i></i></div>
  <div class="field" style="left:54px;top:58px;width:200px"><span>Phone</span><i></i></div>
  <div class="field" style="left:290px;top:58px;width:200px"><span>Date</span><i></i></div>
  <div class="field" style="left:526px;top:58px;width:200px"><span>Time</span><i style="border-radius:50%"></i></div>
  <div class="field" style="left:54px;top:104px;width:672px;height:32px"><span>Message</span></div>
  <div class="btn-block">Book Now</div>
</form>

<section class="gallery abs">
  <h2 class="section-title">Gallery</h2>
</section>
<div class="grid abs">
  <div class="tile" role="img" aria-label="Restaurant interior with lamps" style="background:linear-gradient(135deg,#3a2a22,#8a6a4a)"></div>
  <div class="tile hover"><span class="plus">+</span>Fresh pasta made daily, served with love.</div>
  <div class="tile" role="img" aria-label="Dining room with set tables" style="background:linear-gradient(135deg,#5a3a2a,#c29a6a)"></div>
  <div class="tile" role="img" aria-label="Chef presenting a dish" style="background:linear-gradient(135deg,#6a6a6a,#e8e4dc 60%,#a86a3a)"></div>
  <div class="tile" role="img" aria-label="Plate of pasta with tomatoes" style="background:linear-gradient(135deg,#2a2a2a,#b84a2a 50%,#d88a4a)"></div>
  <div class="tile" role="img" aria-label="Tomatoes and herbs" style="background:linear-gradient(135deg,#4a5a2a,#c23a2a)"></div>
  <div class="tile" role="img" aria-label="Salmon fillet on a board" style="background:linear-gradient(135deg,#d88a5a,#8a5a3a)"></div>
  <div class="tile" role="img" aria-label="Canal view with boats" style="background:linear-gradient(135deg,#8aa0b8,#d6c8b0 50%,#6a5a4a)"></div>
</div>

<footer class="site-footer abs">
  <div class="col abs" style="left:210px">
    <h6>Quick Links</h6>
    <ul class="links"><li>Home</li><li>About Us</li><li>Menu</li><li>Groupmenu</li><li>Reservation</li><li>Contact Us</li></ul>
  </div>
  <div class="col abs" style="left:360px">
    <h6>Contact Address</h6>
    <div class="contact-row"><svg width="12" height="14" viewBox="0 0 12 14"><path d="M6 0a5 5 0 0 1 5 5c0 4-5 9-5 9S1 9 1 5a5 5 0 0 1 5-5z" fill="#ddd"/><circle cx="6" cy="5" r="2" fill="#111"/></svg><span>Teatro Lunaverde<br>Lindengracht 74<br>1016KP Amsterdam</span></div>
    <div class="contact-row" style="font-weight:700;color:#fff"><svg width="12" height="12" viewBox="0 0 10 10"><path d="M2 1l2 2-1 1.2a6 6 0 0 0 2.8 2.8L7 6l2 2-1.4 1.4C4.6 9.2.8 5.4.6 2.4z" fill="#ddd"/></svg>(+31) 20 555 0192</div>
    <div class="contact-row"><svg width="12" height="10" viewBox="0 0 12 10"><rect x="0.5" y="0.5" width="11" height="9" fill="#ddd"/><path d="M.5.5l5.5 5 5.5-5" stroke="#111" fill="none"/></svg>mail@teatrolunaverde.com</div>
  </div>
  <div class="col abs" style="left:585px">
    <h6>Working Hours</h6>
    <table class="hours">
      <tr><td>Monday</td><td>Closed</td></tr>
      <tr><td>Tuesday</td><td>18:00 - 23:00</td></tr>
      <tr><td>Wednesday</td><td>18:00 - 23:00</td></tr>
      <tr><td>Thursday</td><td>18:00 - 23:00</td></tr>
      <tr><td>Friday</td><td>18:00 - 23:00</td></tr>
      <tr><td>Saturday</td><td>18:00 - 23:00</td></tr>
      <tr><td>Sunday</td><td>Closed</td></tr>
    </table>
  </div>
  <div class="col abs news" style="left:835px">
    <h6>Newsletter Signup</h6>
    <input value="Name" readonly>
    <input value="Email" readonly>
    <div class="sub">Subscribe</div>
  </div>
</footer>
<div class="copyright abs">Copyright © 2018 Teatro Lunaverde. All Rights Reserved</div>

</body>
</html>
```